Design for candybags for heapsweets.

I need 3 designs for 3 candybags (3 flavors). Or the same design but different colours
- licorice (black)
- sour (green/yellow ish)
- mix (purple from our website #7F1150)
I want our logo to be in the bags (see nordicpickmix.com) there has to be space in the back of the bag for the bar code and nutritionlist. There has to be a transparent part in the front of the bag, so that you can see the candy in the bag. The size of the bags is 420×594 mm. I want a childish style but at the same time it has to be appealing. I am open minded so if you have a good idea Please let know.

Industry/Entity Type

Food Store

Colors

Designer to choose colors to be used in the design.

Requirements
Must have
• Our logo (www.nordicpickmix.com)
• Space in the back for the nutritionlist and Bar-Code.
• Transparent part at the front side (or back and front) for the customers to be able to see the candy inside.
• The design artwork format has to be in: PSD, AI or CDR.

```html
<!DOCTYPE html>
<html lang="en">
<head>
<meta charset="utf-8">
<title>Mix candy bag – front and back</title>
<link rel="stylesheet" href="https://fonts.googleapis.com/css2?family=Rye&family=Fredoka:wght@600&family=Arimo:wght@400;700&display=swap">
<style>
  :root {
    --bg: #efe6d4;
    --purple: #7f1150;
    --purple-deep: #5e0c3b;
    --purple-light: #9a2468;
    --pink: #e23c78;
    --pink-light: #f0568e;
    --white: #ffffff;
    --ink: #222222;
    --candy-red: #e2343a;
    --candy-green: #9fd19a;
    --candy-yellow: #efe08a;
  }
  * { box-sizing: border-box; margin: 0; padding: 0; }
  html, body { width: 1200px; height: 1200px; overflow: hidden; }
  body { background: var(--bg); position: relative; font-family: "Arimo", Arial, sans-serif; }

  .bag { position: absolute; top: 266px; width: 454px; height: 668px; }
  .bag--front { left: 60px; }
  .bag--back { left: 686px; }
  .bag__art { position: absolute; inset: 0; width: 100%; height: 100%; }

  .brand-name {
    font-family: "Fredoka", sans-serif; font-weight: 600;
    fill: var(--white); text-anchor: middle; letter-spacing: 1px;
  }
  .flavor-title {
    font-family: "Rye", serif; fill: var(--pink-light);
    stroke: var(--white); stroke-width: 3; paint-order: stroke;
    text-anchor: middle;
  }

  .nutrition {
    position: absolute; left: 270px; top: 140px; width: 148px; height: 388px;
    background: var(--white); color: var(--ink); padding: 6px 5px;
    font-size: 6.4px; line-height: 1.3; overflow: hidden;
  }
  .nutrition__title { font-size: 15px; font-weight: 700; line-height: 1; white-space: nowrap; }
  .nutrition__serving { font-size: 6.6px; border-bottom: 6px solid var(--ink); padding-bottom: 2px; }
  .nutrition__row { display: flex; justify-content: space-between; border-bottom: 0.6px solid #777; padding: 1.6px 0; }
  .nutrition__row--thick { border-bottom: 3px solid var(--ink); }
  .nutrition__row--indent { padding-left: 6px; }
  .nutrition__row b { font-weight: 700; }
  .nutrition__note { font-size: 4.8px; border-bottom: 0.6px solid #777; padding: 3px 0 4px; }
  .nutrition__ingredients { font-size: 6.4px; line-height: 1.45; padding-top: 5px; }
</style>
</head>
<body>

<section class="bag bag--front" aria-label="Front of the Mix candy bag">
  <svg class="bag__art" viewBox="0 0 454 668" xmlns="http://www.w3.org/2000/svg">
    <defs>
      <radialGradient id="front-body" cx="50%" cy="45%" r="70%">
        <stop offset="0" stop-color="var(--purple-light)"/>
        <stop offset="1" stop-color="var(--purple-deep)"/>
      </radialGradient>
      <linearGradient id="front-candy" x1="0" y1="0" x2="1" y2="1">
        <stop offset="0" stop-color="var(--candy-green)"/>
        <stop offset="0.35" stop-color="var(--candy-red)"/>
        <stop offset="0.7" stop-color="#c9242c"/>
        <stop offset="1" stop-color="var(--candy-yellow)"/>
      </linearGradient>
    </defs>
    <rect class="bag-body" width="454" height="668" fill="url(#front-body)"/>
    <path class="cloud-band cloud-band--top" fill="var(--pink)"
      d="M0 0H454V124Q430 132 410 110Q380 70 330 60Q290 56 270 40Q240 52 200 44Q170 40 140 54Q100 52 80 70Q60 100 30 118Q14 126 0 120Z"/>
    <rect class="crimp" y="0" width="454" height="26" fill="var(--pink-light)" opacity="0.6"/>
    <path class="cloud-band cloud-band--bottom" fill="var(--pink)"
      d="M0 668H454V560Q430 548 400 570Q370 596 330 586Q290 570 260 584Q230 600 200 588Q160 570 120 580Q80 596 50 570Q24 552 0 562Z"/>
    <rect class="crimp" y="644" width="454" height="24" fill="var(--pink-light)" opacity="0.6"/>

    <g class="brand-mark" transform="translate(226 148)">
      <circle r="86" fill="var(--pink)"/>
      <text class="brand-name" y="-4" font-size="22">NORDIC</text>
      <text class="brand-name" y="22" font-size="22">PICK MIX</text>
    </g>

    <text class="flavor-title" x="227" y="350" font-size="96">MIX</text>

    <path class="candy-window" role="img" aria-label="Transparent window showing the sugared red heart gummy candy inside"
      transform="translate(228 470)" fill="url(#front-candy)" stroke="var(--white)" stroke-opacity="0.5" stroke-width="2"
      d="M0 -62C-22 -112 -124 -104 -124 -22C-124 48 -42 88 0 128C42 88 124 48 124 -22C124 -104 22 -112 0 -62Z"/>
  </svg>
</section>

<section class="bag bag--back" aria-label="Back of the Mix candy bag">
  <svg class="bag__art" viewBox="0 0 454 668" xmlns="http://www.w3.org/2000/svg">
    <defs>
      <radialGradient id="back-body" cx="35%" cy="45%" r="75%">
        <stop offset="0" stop-color="var(--purple-light)"/>
        <stop offset="1" stop-color="var(--purple-deep)"/>
      </radialGradient>
      <linearGradient id="back-candy" x1="0" y1="0" x2="1" y2="1">
        <stop offset="0" stop-color="var(--candy-red)"/>
        <stop offset="0.4" stop-color="var(--candy-green)"/>
        <stop offset="0.65" stop-color="var(--candy-yellow)"/>
        <stop offset="1" stop-color="var(--candy-red)"/>
      </linearGradient>
    </defs>
    <rect class="bag-body" width="454" height="668" fill="url(#back-body)"/>
    <path class="cloud-band cloud-band--top" fill="var(--pink)"
      d="M0 0H454V110Q430 86 400 80Q370 60 340 70Q300 50 260 44Q220 52 190 44Q150 40 120 60Q80 56 60 80Q40 110 20 114Q10 116 0 112Z"/>
    <rect class="crimp" y="0" width="454" height="26" fill="var(--pink-light)" opacity="0.6"/>
    <path class="cloud-band cloud-band--bottom" fill="var(--pink)"
      d="M0 668H454V560Q430 548 400 570Q370 596 330 586Q290 570 260 584Q230 600 200 588Q160 570 120 580Q80 596 50 570Q24 552 0 562Z"/>
    <rect class="crimp" y="644" width="454" height="24" fill="var(--pink-light)" opacity="0.6"/>

    <rect class="back-seam" x="220" y="30" width="32" height="620" fill="var(--pink)"/>
    <line x1="228" y1="30" x2="228" y2="650" stroke="var(--pink-light)" stroke-width="1.5"/>
    <line x1="244" y1="30" x2="244" y2="650" stroke="var(--pink-light)" stroke-width="1.5"/>

    <g class="brand-mark" transform="translate(112 208)">
      <circle r="66" fill="var(--pink)"/>
      <text class="brand-name" y="-3" font-size="16">NORDIC</text>
      <text class="brand-name" y="17" font-size="16">PICK MIX</text>
    </g>

    <text class="flavor-title" x="112" y="372" font-size="74">MIX</text>

    <path class="candy-window" role="img" aria-label="Transparent window showing the mixed sugared gummy candy inside"
      transform="translate(112 470) scale(0.54)" fill="url(#back-candy)"
      d="M0 -62C-22 -112 -124 -104 -124 -22C-124 48 -42 88 0 128C42 88 124 48 124 -22C124 -104 22 -112 0 -62Z"/>
  </svg>

  <div class="nutrition">
    <div class="nutrition__title">Nutrition Facts</div>
    <div class="nutrition__serving">Serving Size 1 fl. oz. (30ml)<br>Servings Per Container 1</div>
    <div class="nutrition__row">Amount Per Serving</div>
    <div class="nutrition__row nutrition__row--thick"><b>Calories 100</b><span>Fat Cal 0</span></div>
    <div class="nutrition__row"><span></span><span>% Daily Value*</span></div>
    <div class="nutrition__row"><span><b>Total Fat</b> 0g</span><span>0%</span></div>
    <div class="nutrition__row nutrition__row--indent"><span>Saturated Fat 0g</span><span>0%</span></div>
    <div class="nutrition__row nutrition__row--indent"><span>Trans Fat 0g</span><span>0%</span></div>
    <div class="nutrition__row"><span><b>Cholesterol</b> 0g</span><span>0%</span></div>
    <div class="nutrition__row"><span><b>Sodium</b> 35mg</span><span>2%</span></div>
    <div class="nutrition__row"><span><b>Potassium</b> 10mg</span><span>0%</span></div>
    <div class="nutrition__row"><span><b>Total Carbohydrate</b> 10g</span><span>4%</span></div>
    <div class="nutrition__row nutrition__row--indent"><span>Dietary Fiber 2g</span><span>8%</span></div>
    <div class="nutrition__row nutrition__row--indent"><span>Sugars 3g</span><span></span></div>
    <div class="nutrition__row nutrition__row--thick"><span><b>Protein</b> 15g</span><span></span></div>
    <div class="nutrition__note">*Percent Daily Values are based on a 2,000 calorie diet. Your daily values may be higher or lower depending on your calorie needs.</div>
    <div class="nutrition__ingredients"><b>Ingredients</b> Pure deionized water, protein blend of hydrolyzed collagen, whey protein isolate (milk) and casein protein isolate (milk), pear juice concentrate, glycerol, chicory vegetable fiber, malic acid, natural flavors, carrageenan, acesulfame-potassium, sucralose, red 40, blue 1.</div>
  </div>
</section>

</body>
</html>
```